FinTech company looking to revamp and expand client-facing interface for our financial models

Halvern Quotient currently has a very simple website that allows clients to interact with our financial models. We are looking to completely redesign the current site and add several extra pages to provide extra functionality. We want the design to have a modern, slick feel, that will work on both a desktop or a tablet. It should be straightforward for clients to move between different pages at any time, and clear from the layout how to interact with the more advanced features. We have included screenshots of existing pages in the attached design brief, as well as sketches of the functionality required by the new pages, but can't provide a direct link to the current site.
Target Market(s)
Professional investors that will be paying to access the interface
Industry/Entity Type
Finance
Number of Pages Required
4 page
Colors
Designer to choose colors to be used in the design.
Look and feel
Each slider illustrates characteristics of the customer's brand and the style your logo design should communicate.

```html
<!DOCTYPE html>
<html lang="en">
<head>
<meta charset="utf-8">
<title>Halvern Quotient – Models</title>
<link href="https://fonts.googleapis.com/css2?family=Lato:wght@300;400;700&family=Montserrat:wght@300;400;500;700&display=swap" rel="stylesheet">
<style>
:root{
  --navy:#051628;
  --navy-band:#0b2540;
  --red:#d8263d;
  --blue:#0a9cf5;
  --blue-light:#3db4f9;
  --blue-deep:#0a8de6;
  --row-blue:#eef6f9;
  --row-pink:#fbeeee;
  --ink:#2b2b2b;
  --rule:#d9d9d9;
  --star:#f0901e;
  --plus:#1a9be0;
  --white:#ffffff;
}
*{box-sizing:border-box;margin:0;padding:0}
html,body{width:1013px;height:1200px;overflow:hidden;background:var(--white)}
body{font-family:'Lato',sans-serif;color:var(--ink)}
.stage{position:absolute;left:0;top:0;width:1318px;height:1572px;transform:scale(.7686,.7634);transform-origin:0 0}
.abs{position:absolute}

/* sidebar */
.sidebar{position:absolute;background:var(--navy);font-family:'Montserrat',sans-serif;color:var(--white)}
.brand{position:absolute;font-family:'Montserrat',sans-serif;font-weight:300;color:var(--white);letter-spacing:1px}
.user-band{position:absolute;background:var(--navy-band)}
.avatar{position:absolute;border-radius:50%;background:linear-gradient(135deg,#8f7ee8,#e98a6a)}
.nav-item{position:absolute;font-size:15px;font-weight:700;letter-spacing:.3px}
.nav-sub{position:absolute;font-size:14px;font-weight:400;color:#c9d2dc}
.nav-active{position:absolute;background:var(--red)}
.chev{position:absolute;width:18px;height:18px}
.toggle{position:absolute;background:var(--navy);border-radius:0 22px 22px 0}

/* main */
.page-title{position:absolute;font-family:'Montserrat',sans-serif;font-weight:400;font-size:28px;color:#333}
.rule{position:absolute;height:1px;background:var(--rule)}
.label{position:absolute;font-size:16px;color:#333}
.label big{font-size:18px}
.field{position:absolute;width:157px;height:26px;border:1.5px solid #3aa6ee;border-radius:4px;background:var(--white)}
.export{position:absolute;color:var(--red);font-size:18px;display:flex;align-items:center;gap:9px}

/* tables */
.grid-row{position:absolute;display:grid;align-items:center;text-align:center;font-size:12px}
.grid-row span{display:flex;align-items:center;justify-content:center;height:100%;line-height:1.4}
.head{color:var(--white);font-size:13px;font-weight:400;background:var(--blue)}
.top-cols{grid-template-columns:74px 113px 110px 80px 70px 72px 68px 70px 74px 79px;width:810px}
.bottom-cols{grid-template-columns:92px 89px 100px 101px 98px 95px 98px 96px 93px 84px;width:946px}
.row-blue{background:var(--row-blue)}
.row-pink{background:var(--row-pink)}
.btn-more{position:absolute;background:var(--red);color:var(--white);font-size:12px;display:flex;align-items:center;justify-content:center;border-radius:0 3px 3px 0}
.table-frame{position:absolute;border:1px solid #e4e8ea}
.data-wash{position:absolute;background:linear-gradient(160deg,var(--blue-light),var(--blue-deep))}
.light-head span{background:var(--row-blue);color:#333}
.light-head span.id-head{background:var(--blue);color:var(--white)}
.on-blue span{color:var(--white)}
.on-blue span.id-cell{color:#333}
.star{position:absolute;width:28px;height:30px}
</style>
</head>
<body>
<svg width="0" height="0" style="position:absolute">
  <defs>
    <symbol id="fav" viewBox="0 0 28 30">
      <path d="M12 8l3 6.5 7 .8-5.2 4.8 1.4 7L12 23.6 5.8 27.1l1.4-7L2 15.3l7-.8z" fill="var(--star)"/>
      <path d="M20 1v10M15 6h10" stroke="var(--plus)" stroke-width="2.6"/>
    </symbol>
    <symbol id="down" viewBox="0 0 18 18"><path d="M2 6l7 7 7-7" fill="none" stroke="currentColor" stroke-width="1.6"/></symbol>
    <symbol id="right" viewBox="0 0 18 18"><path d="M6 2l7 7-7 7" fill="none" stroke="currentColor" stroke-width="1.6"/></symbol>
    <symbol id="share" viewBox="0 0 22 20"><path d="M8 4H2v14h15v-5" fill="none" stroke="#444" stroke-width="1.5"/><path d="M7 13c1-5 5-7 10-7M14 2l4 4-4 4" fill="none" stroke="#444" stroke-width="1.5"/></symbol>
  </defs>
</svg>

<div class="stage">

<!-- ===== Expanded navigation view ===== -->
<aside class="sidebar" style="left:0;top:0;width:307px;height:768px">
  <div class="brand" style="left:97px;top:26px;font-size:38px">HALVERN</div>
  <div class="user-band" style="left:0;top:97px;width:307px;height:53px"></div>
  <div class="avatar" role="img" aria-label="User avatar illustration" style="left:62px;top:104px;width:38px;height:38px"></div>
  <div class="abs" style="left:111px;top:116px;font-size:15px;font-weight:500">Username</div>

  <div class="nav-item" style="left:58px;top:176px">250D</div>
  <svg class="chev" style="left:227px;top:177px;color:#fff"><use href="#down"/></svg>
  <div class="nav-item" style="left:58px;top:212px">MODELS</div>
  <svg class="chev" style="left:227px;top:213px;color:#fff"><use href="#down"/></svg>
  <div class="nav-sub" style="left:57px;top:246px">EQUITIES</div>
  <div class="nav-sub" style="left:57px;top:280px">EFTS</div>
  <div class="nav-active" style="left:0;top:303px;width:307px;height:38px"></div>
  <div class="nav-sub" style="left:57px;top:314px;color:#fff">EFT PAIRS</div>
  <div class="nav-sub" style="left:57px;top:348px">PAIRS</div>
  <div class="nav-item" style="left:58px;top:381px">SENSETIVES</div>
  <svg class="chev" style="left:227px;top:382px;color:#fff"><use href="#right"/></svg>
  <div class="nav-item" style="left:58px;top:416px">FAVOURITES</div>
  <svg class="chev" style="left:227px;top:417px;color:#fff"><use href="#right"/></svg>
  <div class="nav-item" style="left:58px;top:450px">42D</div>
  <svg class="chev" style="left:227px;top:451px;color:#fff"><use href="#right"/></svg>
  <div class="nav-item" style="left:58px;top:484px">83D</div>
  <svg class="chev" style="left:227px;top:485px;color:#fff"><use href="#right"/></svg>
</aside>
<div class="toggle" style="left:300px;top:25px;width:46px;height:38px"></div>
<svg class="chev" style="left:310px;top:33px;width:22px;height:22px;color:#fff"><path d="M15 2L6 11l9 9" fill="none" stroke="#fff" stroke-width="1.8"/></svg>

<h1 class="page-title" style="left:368px;top:45px">MODELS</h1>
<div class="rule" style="left:316px;top:85px;width:922px"></div>

<div class="label" style="left:370px;top:130px">Quality &nbsp;&nbsp;&nbsp;&nbsp;Threshold :</div>
<div class="field" style="left:524px;top:128px"></div>
<div class="label" style="left:371px;top:187px"><big>Abs.</big> Stat &nbsp;&nbsp;Threshold :</div>
<div class="field" style="left:524px;top:187px"></div>

<div class="export" style="left:371px;top:276px"><svg width="22" height="20"><use href="#share"/></svg>Export</div>

<div class="table-frame" style="left:370px;top:304px;width:812px;height:355px"></div>
<div class="grid-row head top-cols" style="left:371px;top:304px;height:46px">
  <span>ID&nbsp;<svg width="12" height="12" style="color:#fff"><use href="#down"/></svg></span><span>SECTOR</span><span>TIME</span><span>Quality</span><span>Stat 1</span><span>Stat 1</span><span>Stat 2</span><span>Stat 3</span><span>Stat 4</span><span>Stat 5</span>
</div>
<div class="btn-more" style="left:1181px;top:304px;width:50px;height:46px">More</div>

<div class="grid-row top-cols row-blue" style="left:371px;top:350px;height:61px"><span>Modal1</span><span>Materials</span><span>2019-07-3<br>12:15.00.000</span><span>30.2288</span><span>2.01754</span><span>23.305</span><span>23.305</span><span>-0.149368</span><span>22.3054</span><span>4.63714</span></div>
<div class="grid-row top-cols row-pink" style="left:371px;top:411px;height:62px"><span>Modal 2</span><span>Industrials</span><span>2019-07-3<br>12:15.00.000</span><span>32.8694</span><span>0.87307</span><span>32.185</span><span>-0.0336927</span><span>33.9911</span><span>11.5693</span><span>0.472968</span></div>
<div class="grid-row top-cols row-blue" style="left:371px;top:473px;height:61px"><span>Modal3</span><span>Consumer<br>Discretionary</span><span>2019-07-3<br>12:15.00.000</span><span>1.66002</span><span>-0.569222</span><span>159.814</span><span>0.0252328</span><span>172.616</span><span>10.2875</span><span>-0.750396</span></div>
<div class="grid-row top-cols row-pink" style="left:371px;top:534px;height:62px"><span>Modal4</span><span>Information<br>Technology</span><span>2019-07-3<br>12:15.00.000</span><span>46.6856</span><span>0.412148</span><span>202.488</span><span>0.00849232</span><span>205.834</span><span>11.9094</span><span>-1.0.137913</span></div>
<div class="grid-row top-cols row-blue" style="left:371px;top:596px;height:62px"><span>Modal5</span><span>Information<br>Technology</span><span>2019-07-3<br>12:15.00.000</span><span>75.7733</span><span>7.06728</span><span>188.605</span><span>0.016913</span><span>181.665</span><span>3.82241</span><span>0.9819096</span></div>

<svg class="star" style="left:336px;top:364px"><use href="#fav"/></svg>
<svg class="star" style="left:336px;top:425px"><use href="#fav"/></svg>
<svg class="star" style="left:336px;top:486px"><use href="#fav"/></svg>
<svg class="star" style="left:336px;top:550px"><use href="#fav"/></svg>
<svg class="star" style="left:336px;top:610px"><use href="#fav"/></svg>

<!-- ===== Collapsed navigation view ===== -->
<aside class="sidebar" style="left:0;top:768px;width:95px;height:804px">
  <div class="brand" style="left:8px;top:26px;font-size:20px">HALVERN</div>
  <div class="user-band" style="left:0;top:102px;width:95px;height:56px"></div>
  <div class="avatar" role="img" aria-label="User avatar illustration" style="left:29px;top:111px;width:40px;height:40px"></div>
  <div class="nav-item" style="left:23px;top:189px;font-size:16px">250D</div>
  <div class="nav-item" style="left:27px;top:253px;font-size:16px">42D</div>
  <div class="nav-item" style="left:27px;top:323px;font-size:16px">83D</div>
</aside>
<div class="toggle" style="left:90px;top:823px;width:46px;height:40px"></div>
<svg class="chev" style="left:104px;top:831px;width:22px;height:22px"><path d="M6 2l9 9-9 9" fill="none" stroke="#fff" stroke-width="1.8"/></svg>

<h1 class="page-title" style="left:273px;top:810px">MODELS</h1>
<div class="rule" style="left:181px;top:852px;width:1137px"></div>

<div class="label" style="left:275px;top:900px">Quality &nbsp;&nbsp;&nbsp;&nbsp;&nbsp;Threshold :</div>
<div class="field" style="left:438px;top:898px;width:165px"></div>
<div class="label" style="left:276px;top:961px"><big>Abs.</big> Stat &nbsp;&nbsp;Threshold :</div>
<div class="field" style="left:438px;top:960px;width:165px"></div>

<div class="export" style="left:276px;top:1055px"><svg width="22" height="20"><use href="#share"/></svg>Export</div>

<div class="table-frame" style="left:275px;top:1083px;width:948px;height:375px"></div>
<div class="data-wash" style="left:368px;top:1132px;width:854px;height:325px"></div>
<div class="grid-row bottom-cols light-head" style="left:276px;top:1084px;height:48px;font-size:14px">
  <span class="id-head">ID&nbsp;<svg width="12" height="12" style="color:#fff"><use href="#down"/></svg></span><span>Stat 6</span><span>Stat7</span><span>Stat 8</span><span>Stat 9</span><span>Stat 10</span><span>Stat 11</span><span>Stat 12</span><span>Stat 13</span><span>Stat 14</span>
</div>
<div class="btn-more" style="left:1223px;top:1084px;width:53px;height:48px">Less</div>

<div class="grid-row bottom-cols on-blue" style="left:276px;top:1132px;height:65px"><span class="id-cell row-blue">Modal1</span><span>0.945706</span><span>2.81949</span><span>2.60858</span><span>30.2288</span><span>2.01754</span><span>23.305</span><span>23.305</span><span>-0.149368</span><span>22.3054</span></div>
<div class="grid-row bottom-cols on-blue" style="left:276px;top:1197px;height:65px"><span class="id-cell row-pink">Modal 2</span><span>-0.472968</span><span>-0.830458</span><span>6.80646</span><span>32.8694</span><span>0.87307</span><span>32.185</span><span>-0.0336927</span><span>33.9911</span><span>11.5693</span></div>
<div class="grid-row bottom-cols on-blue" style="left:276px;top:1262px;height:65px"><span class="id-cell row-blue">Modal3</span><span>-0.750396</span><span>-0.385309</span><span>4.69146</span><span>1.66002</span><span>-0.569222</span><span>159.814</span><span>0.0252328</span><span>172.616</span><span>10.2875</span></div>
<div class="grid-row bottom-cols on-blue" style="left:276px;top:1327px;height:65px"><span class="id-cell row-pink">Modal4</span><span>0.137913</span><span>0.449595</span><span>3.85106</span><span>46.6856</span><span>0.412148</span><span>202.488</span><span>0.00849232</span><span>205.834</span><span>11.9094</span></div>
<div class="grid-row bottom-cols on-blue" style="left:276px;top:1392px;height:65px"><span class="id-cell row-blue">Modal5</span><span>0.981019</span><span>1.29847</span><span>3.35927</span><span>75.7733</span><span>7.06728</span><span>188.605</span><span>0.016913</span><span>181.665</span><span>3.82241</span></div>

<svg class="star" style="left:241px;top:1147px"><use href="#fav"/></svg>
<svg class="star" style="left:241px;top:1211px"><use href="#fav"/></svg>
<svg class="star" style="left:241px;top:1276px"><use href="#fav"/></svg>
<svg class="star" style="left:241px;top:1342px"><use href="#fav"/></svg>
<svg class="star" style="left:241px;top:1406px"><use href="#fav"/></svg>

</div>
</body>
</html>
```